Business Card Project

We are a small consulting firm. You can experiment with any design.
Must have:
1) Company name - TOLVIN International
2) Company slogan - simple solutions for complex problems
3) Name/Title/Phone/Email/WWW/ - use anything you like as an example.

Industry/Entity Type

Business

```html
<!DOCTYPE html>
<html lang="en">
<head>
<meta charset="utf-8">
<title>TOLVIN International – Business Cards</title>
<link href="https://fonts.googleapis.com/css2?family=Open+Sans:wght@400&display=swap" rel="stylesheet">
<style>
  :root {
    --backdrop: #e6e3df;
    --card-dark: #1c1e23;
    --card-light: #ffffff;
    --text-light: #f2f2f2;
    --text-slogan: #8a8c90;
    --text-dark: #4a4a4a;
    --text-muted: #9a9a9a;
    --text-body: #5c5c5c;
    --accent: #2a8fd8;
    --shadow: rgba(0, 0, 0, 0.28);
  }
  * { margin: 0; padding: 0; box-sizing: border-box; }
  html, body {
    width: 1200px;
    height: 684px;
    overflow: hidden;
    background: var(--backdrop);
    font-family: "Open Sans", Verdana, sans-serif;
  }
  .canvas { position: relative; width: 1200px; height: 684px; }

  .card {
    position: absolute;
    box-shadow: 0 3px 8px var(--shadow);
  }

  /* Front */
  .card-front {
    left: 160px; top: 144px;
    width: 420px; height: 256px;
    background: var(--card-dark);
  }
  .card-front .brand {
    position: absolute;
    left: 62px; top: 80px;
    display: flex; align-items: center; gap: 14px;
  }
  .card-front .brand-dot {
    width: 40px; height: 40px; border-radius: 50%;
    background: var(--accent);
  }
  .card-front .brand-name {
    color: var(--text-light);
    font-size: 26px;
    letter-spacing: 1px;
    text-transform: uppercase;
    line-height: 1;
  }
  .card-front .slogan {
    position: absolute;
    left: 64px; top: 144px;
    color: var(--text-slogan);
    font-size: 14.5px;
    letter-spacing: 0.3px;
  }

  /* Back */
  .card-back {
    left: 627px; top: 296px;
    width: 426px; height: 260px;
    background: var(--card-light);
  }
  .card-back .brand {
    position: absolute;
    left: 32px; top: 38px;
    display: flex; align-items: center; gap: 9px;
  }
  .card-back .brand-dot {
    width: 26px; height: 26px; border-radius: 50%;
    background: var(--accent);
  }
  .card-back .brand-name {
    color: var(--text-dark);
    font-size: 17px;
    letter-spacing: 0.6px;
    text-transform: uppercase;
    line-height: 1;
  }
  .card-back .accent-bar {
    position: absolute;
    right: 0; top: 119px;
    width: 5px; height: 115px;
    background: var(--accent);
  }
  .card-back .person {
    position: absolute;
    right: 32px; top: 114px;
    text-align: right;
  }
  .card-back .person-name {
    color: var(--text-dark);
    font-size: 16px;
    letter-spacing: 0.5px;
    text-transform: uppercase;
  }
  .card-back .person-title {
    color: var(--text-muted);
    font-size: 12px;
    letter-spacing: 0.4px;
    margin-top: 1px;
  }
  .card-back .contact {
    position: absolute;
    right: 29px; top: 174px;
    list-style: none;
    text-align: right;
    color: var(--text-body);
    font-size: 10.5px;
  }
  .card-back .contact li { height: 25px; line-height: 15px; }
  .card-back .website {
    position: absolute;
    left: 30px; top: 224px;
    color: var(--accent);
    font-size: 10.5px;
    line-height: 15px;
  }
</style>
</head>
<body>
<main class="canvas">
  <section class="card card-front" aria-label="Business card front">
    <div class="brand">
      <span class="brand-dot"></span>
      <span class="brand-name">TOLVIN International</span>
    </div>
    <p class="slogan">Simple Solutions For Complex Problems</p>
  </section>

  <section class="card card-back" aria-label="Business card back">
    <div class="brand">
      <span class="brand-dot"></span>
      <span class="brand-name">TOLVIN International</span>
    </div>
    <div class="accent-bar"></div>
    <div class="person">
      <p class="person-name">Marco Vellan</p>
      <p class="person-title">Creative Director</p>
    </div>
    <ul class="contact">
      <li>2871 Harbor Crest Lane</li>
      <li>mail@tolvinhq.com</li>
      <li>0198 765 432</li>
    </ul>
    <p class="website">www.tolvinhq.com</p>
  </section>
</main>
</body>
</html>
```